SEO marketing site

I need a design only for an SEO/Marketing project I have in mind. I have bought the domain Brovelle.example and want to aim this project at businesses who want to push their business further. WHEN I SAY DESIGN ONLY, I MEAN NO PROGRAMMING. HOWEVER, I DO NEED THE DESIGNER TO PUT THIS SITE ONLINE. $300 IS A LOT OF MONEY FOR A TEMPLATE YOU CAN PURCHASE FOR $60 WITH SOME CUSTOMISATION.

The idea is that businesses will register with us and will be offered two different kinds of services. They can make use of our scripts to check their back links, rankings, compare with competitors and a number of other marketing tools. The other service we provide is that we offer them an SEO service at a very competitive price. We will handle social networking, link building, article submission, directory submission, social bookmarking etc etc at a reasonable monthly fee.

I quorix tiled look/flat design is what I really like, and I want to give off a professional vibe. This is the kind of site I wish to go for.

JUST TO REPEAT, I NEED A DESIGN TO BE PUT ONLINE, I.E PSD TO HTML CONVERSION. MY PROGRAMMERS WILL CODE THE CLIENT AREA THEMSELVES.

Target Market(s)

Other businesses

Industry/Entity Type

Marketing

Requirements
Must have
• Quorix 5 or flat design look. Even a site, similar to plumtower, is quite attractive. I would like a killer design for the site.

```html
<!DOCTYPE html>
<html lang="en">
<head>
<meta charset="utf-8">
<title>Brovelle.example — SEO &amp; Marketing Services</title>
<link href="https://fonts.googleapis.com/css2?family=Exo:wght@300;400;500;600&family=Open+Sans:wght@400;600;700&family=Caveat:wght@500&display=swap" rel="stylesheet">
<style>
:root{
  --green:#7ab648;
  --green-dark:#5e9632;
  --blue:#3b94d0;
  --ink:#2b2b2b;
  --charcoal:#333536;
  --text:#555;
  --muted:#888;
  --sky-top:#d9ecf8;
  --sky-bottom:#f4f9fc;
  --panel:#f0f0f0;
  --white:#fff;
  --red:#e0452d;
  --orange:#f39a1e;
  --navy:#1f4e79;
}
*{margin:0;padding:0;box-sizing:border-box}
html,body{width:1200px;height:2444px;overflow:hidden}
body{position:relative;background:var(--white);font-family:"Open Sans",Arial,sans-serif;color:var(--text);font-size:15px}
.abs{position:absolute}

/* header */
.site-header{left:0;top:0;width:1200px;height:88px;background:var(--ink)}
.brand{left:183px;top:24px;display:flex;align-items:center;gap:10px;font-family:"Exo",sans-serif;font-weight:500;font-size:30px;color:var(--green)}
.brand-dot{width:30px;height:30px;border-radius:50%;background:var(--green)}
.main-nav{left:575px;top:16px;display:flex;gap:26px}
.nav-item{display:flex;flex-direction:column;align-items:center;gap:6px;color:var(--white);font-size:14px}
.nav-icon{width:26px;height:26px;border-radius:50%;border:2px solid var(--white)}

/* hero */
.hero{left:0;top:88px;width:1200px;height:450px;background:linear-gradient(180deg,var(--sky-top),var(--sky-bottom))}
.hero-art{left:470px;top:205px;width:600px;height:333px;background:radial-gradient(ellipse at 50% 45%,#c6e3a6 0%,#a9d4ea 40%,rgba(217,236,248,0) 72%)}
.hero-title{left:197px;top:112px;font-family:"Exo",sans-serif;font-weight:400;color:var(--ink);font-size:31px;line-height:1.25;letter-spacing:.5px}
.hero-title .big{font-size:41px}
.account-links{left:858px;top:110px;display:flex;background:var(--charcoal);color:var(--white);font-size:13px;padding:6px 14px;gap:18px}
.testimonial{left:201px;top:225px;width:215px;background:#3d3f40;color:#e5e5e5;padding:16px 14px 12px 34px;font-size:11px;line-height:1.4}
.testimonial .quote{left:10px;top:8px;font-size:34px;color:var(--white);font-family:Georgia,serif;line-height:1}
.testimonial .author{display:block;text-align:right;color:var(--green);font-size:10px;line-height:1.3;margin-top:8px}
.testimonial .more{display:block;text-align:right;color:var(--white);font-size:9px;font-weight:700;margin-top:12px}

/* cta band */
.cta-band{left:0;top:538px;width:1200px;height:85px;background:var(--green)}
.cta-text{left:176px;top:552px;color:var(--white);font-family:"Exo",sans-serif}
.cta-text h2{font-size:32px;font-weight:400;line-height:1.1}
.cta-text p{font-size:19px;font-weight:400}
.cta-signup{left:794px;top:538px;width:208px;height:85px;background:var(--ink);color:var(--white);text-align:center;font-family:"Exo",sans-serif;padding-top:12px}
.cta-signup strong{display:block;font-size:34px;font-weight:400;line-height:1}
.cta-signup span{font-size:11px;letter-spacing:2px}
.newsletter{left:0;top:623px;width:1200px;height:86px;background:linear-gradient(180deg,#fff 60%,#ececec)}
.newsletter-text{left:220px;top:648px;font-size:13px;color:var(--ink)}
.newsletter-form{left:628px;top:638px;display:flex;border:2px solid var(--green)}
.newsletter-form .field{width:242px;height:32px;padding:6px 8px;font-size:13px;color:#aaa;background:var(--white)}
.newsletter-form .send{width:96px;height:32px;background:var(--green);color:var(--white);font-size:11px;font-weight:700;text-align:center;line-height:32px}

/* services */
.tagline{font-family:"Caveat",cursive;color:var(--blue);font-size:22px}
.section-title{font-family:"Exo",sans-serif;font-weight:400;color:var(--ink);font-size:40px;line-height:1}
.section-title .accent{color:var(--green)}
.lead{font-size:13px;line-height:1.5;color:var(--text)}
.sub-title{font-family:"Exo",sans-serif;color:var(--green);font-size:29px;font-weight:400}
.steps{list-style:none}
.steps li{display:flex;align-items:center;gap:12px;font-size:13px;color:var(--ink);height:25px}
.steps .num{width:20px;height:20px;border-radius:50%;background:var(--blue);color:var(--white);font-size:11px;font-weight:700;display:flex;align-items:center;justify-content:center}
.btn{display:inline-block;width:142px;height:36px;line-height:36px;text-align:center;color:var(--white);font-size:12px;font-weight:600}
.btn-green{background:var(--green)}
.btn-blue{background:var(--blue)}
.seo-art{left:640px;top:720px;width:420px;height:478px;background:radial-gradient(ellipse at 50% 55%,#8cc05c 0%,#c9d7bb 42%,rgba(255,255,255,0) 70%)}
.divider{left:0;width:1200px;height:30px;background:radial-gradient(ellipse at 50% 0,rgba(0,0,0,.12),rgba(0,0,0,0) 70%)}

.flow-label{font-size:10.5px;line-height:1.35;color:var(--text);width:135px}
.flow-label b{display:block;color:var(--navy);font-size:11.5px}

/* coverage */
.coverage{left:0;top:1723px;width:1200px;height:391px;background:var(--panel);border-top:1px solid #e2e2e2}
.coverage-title{left:0;top:1736px;width:1200px;text-align:center;font-family:"Exo",sans-serif;font-weight:400;color:var(--green);font-size:33px}
.cover-list{left:182px;top:1816px;display:flex}
.cover-item{width:140px;display:flex;flex-direction:column;align-items:center;gap:12px;font-size:14px;color:var(--ink)}
.cover-item svg{width:94px;height:94px}
.signup-btn{left:501px;top:1984px;width:208px;height:49px;background:var(--blue);color:var(--white);font-size:19px;text-align:center;line-height:49px;font-family:"Exo",sans-serif}

/* footer */
.footer-col h4{font-size:16px;font-weight:600;color:var(--ink);margin-bottom:14px}
.footer-col li{list-style:none;font-size:11px;line-height:22px;color:var(--text)}
.footer-about{width:370px;font-size:11px;line-height:1.55}
.socials{display:flex;gap:12px}
.socials span{width:22px;height:22px;border-radius:50%;background:var(--green-dark)}
.bottom-bar{left:0;top:2366px;width:1200px;height:78px;background:var(--ink)}
.bottom-brand{left:183px;top:2389px;display:flex;align-items:center;gap:8px;font-family:"Exo",sans-serif;font-size:26px;color:var(--green)}
.bottom-brand .brand-dot{width:26px;height:26px}
.copyright{left:0;top:2400px;width:1200px;text-align:center;font-size:11px;color:#bbb}
</style>
</head>
<body>

<header class="abs site-header"></header>
<div class="abs brand"><span class="brand-dot"></span>brovelle.example</div>
<nav class="abs main-nav">
  <a class="nav-item"><span class="nav-icon"></span>Home</a>
  <a class="nav-item"><span class="nav-icon"></span>Features</a>
  <a class="nav-item"><span class="nav-icon"></span>Plans &amp; Pricing</a>
  <a class="nav-item"><span class="nav-icon"></span>Blog</a>
  <a class="nav-item"><span class="nav-icon"></span>SEO</a>
  <a class="nav-item"><span class="nav-icon"></span>SEM</a>
</nav>

<section class="abs hero"></section>
<div class="abs hero-art" role="img" aria-label="Illustration of hands holding a tablet with colourful speech bubbles for SEO, SEM, link building, article submission and social bookmarking"></div>
<h1 class="abs hero-title">IMPROVE YOUR <span class="big">BRAND VISIBILITY</span><br>USING OUR SERVICES</h1>
<div class="abs account-links"><span>Signin</span><span>Register</span></div>
<blockquote class="abs testimonial">
  <span class="abs quote">&#8220;</span>
  wow! these folks are amazing to work with, when we saw amazing yes we mean it!! by using their services our business getting numerous leads. They improved our search engine ranking and we are listing on the first page!! We always recommended them to everyone and friends.
  <span class="author">Mara Lindqvist,<br>abc Inc, USA</span>
  <span class="more">MORE TESTIMONIALS</span>
</blockquote>

<section class="abs cta-band"></section>
<div class="abs cta-text"><h2>Contact brovelle now!</h2><p>We Are A Search Engine optimization &amp; Marketing Specialists.</p></div>
<div class="abs cta-signup"><strong>SignUp</strong><span>CLICK HERE</span></div>
<div class="abs newsletter"></div>
<p class="abs newsletter-text">Get brovelle's FREE email newsletter, be the First to know!!</p>
<div class="abs newsletter-form"><span class="field">Your email</span><span class="send">SUBMIT</span></div>

<!-- SEO -->
<div class="abs seo-art" role="img" aria-label="Isometric illustration of green blocks with a mobile device, growth chart, lifebuoy and support labels"></div>
<div class="abs tagline" style="left:362px;top:743px">Search Engine Optimization</div>
<h2 class="abs section-title" style="left:176px;top:770px"><span class="accent">SEO</span> Services</h2>
<p class="abs lead" style="left:176px;top:825px;width:450px">Getting listed in search engines is not a difficult task but what matters is how your site has been listed in a search engine and how well you are ranked. Your site can get higher rankings in all search engines if you follow ethical seo strategies.</p>
<h3 class="abs sub-title" style="left:176px;top:905px">How we are different</h3>
<ul class="abs steps" style="left:176px;top:960px">
  <li><span class="num">1</span>Prepare a tailor made SEO &amp; SEM proposal</li>
  <li><span class="num">2</span>Monthly Ranking/ Progress Reports sent to client</li>
  <li><span class="num">3</span>Strict monthly maintenace plans</li>
  <li><span class="num">4</span>24/7 hours client support is provided</li>
</ul>
<a class="abs btn btn-green" style="left:176px;top:1098px">LEARN MORE</a>
<a class="abs btn btn-blue" style="left:335px;top:1098px">APPLY NOW</a>

<div class="abs divider" style="top:1222px"></div>

<!-- SEM -->
<svg class="abs" style="left:208px;top:1320px" width="392" height="270" viewBox="0 0 392 270" aria-hidden="true">
  <g fill="none" stroke-width="2" stroke-dasharray="5 4">
    <path d="M97 50 Q150 60 150 140" stroke="#e0452d"/>
    <path d="M232 50 Q182 60 182 140" stroke="#f39a1e"/>
    <path d="M97 200 Q148 196 148 162" stroke="#7ab648"/>
    <path d="M232 200 Q184 196 184 162" stroke="#3b94d0"/>
  </g>
  <rect x="19" y="12" width="78" height="73" fill="#e0452d"/>
  <rect x="232" y="12" width="78" height="73" fill="#f39a1e"/>
  <rect x="19" y="166" width="78" height="78" fill="#7ab648"/>
  <rect x="232" y="166" width="78" height="78" fill="#3b94d0"/>
  <circle cx="166" cy="151" r="25" fill="#1f4e79"/>
  <rect x="156" y="141" width="20" height="20" fill="#fff"/>
</svg>
<div class="abs flow-label" style="left:212px;top:1410px"><b>Boost Your ROI</b>Lorem Ipsum is simply dummy text of the printing and typesetting</div>
<div class="abs flow-label" style="left:428px;top:1410px"><b>Delivering Results</b>Lorem Ipsum is simply dummy text of the printing and typesetting</div>
<div class="abs flow-label" style="left:212px;top:1570px"><b>Acquire new customers</b>Lorem Ipsum is simply dummy text of the printing and typesetting</div>
<div class="abs flow-label" style="left:405px;top:1570px;width:180px"><b>Competitive Research &amp; Analysis</b>Lorem Ipsum is simply dummy text of the printing and typesetting</div>

<div class="abs tagline" style="left:833px;top:1272px">Search Engine Marketing</div>
<h2 class="abs section-title" style="left:623px;top:1300px"><span class="accent">SEM</span> Services</h2>
<p class="abs lead" style="left:623px;top:1350px;width:430px">Getting listed in search engines is not a difficult task but what matters is how your site has been listed in a search engine and how well you are ranked. Your site can get higher rankings in all search engines if you follow ethical seo strategies.</p>
<h3 class="abs sub-title" style="left:623px;top:1428px">How we are different</h3>
<ul class="abs steps" style="left:623px;top:1476px">
  <li><span class="num">1</span>Prepare a tailor made SEO &amp; SEM proposal</li>
  <li><span class="num">2</span>Monthly Ranking/ Progress Reports sent to client</li>
  <li><span class="num">3</span>Strict monthly maintenace plans</li>
  <li><span class="num">4</span>24/7 hours client support is provided</li>
</ul>
<a class="abs btn btn-green" style="left:623px;top:1620px">LEARN MORE</a>
<a class="abs btn btn-blue" style="left:775px;top:1620px">APPLY NOW</a>

<!-- coverage -->
<section class="abs coverage"></section>
<h2 class="abs coverage-title">See What Our Services Cover</h2>
<div class="abs cover-list">
  <div class="cover-item">
    <svg viewBox="0 0 94 94" aria-hidden="true"><rect width="94" height="94" fill="#d5d5d5"/><path d="M22 34h8l7 26h28l6-20H33" fill="none" stroke="#555" stroke-width="5"/><circle cx="40" cy="68" r="4" fill="#555"/><circle cx="62" cy="68" r="4" fill="#555"/></svg>
    Social Networking</div>
  <div class="cover-item">
    <svg viewBox="0 0 94 94" aria-hidden="true"><g fill="none" stroke="#7ab648" stroke-width="7"><rect x="18" y="38" width="32" height="18" rx="9" transform="rotate(-40 34 47)"/><rect x="44" y="38" width="32" height="18" rx="9" transform="rotate(-40 60 47)"/></g></svg>
    Link Building</div>
  <div class="cover-item">
    <svg viewBox="0 0 94 94" aria-hidden="true"><rect x="24" y="18" width="42" height="58" fill="none" stroke="#7ab648" stroke-width="5"/><path d="M32 34h26M32 46h26M32 58h16" stroke="#7ab648" stroke-width="4"/><path d="M52 64l22-30 6 4-22 30z" fill="#5e9632"/></svg>
    Article Submission</div>
  <div class="cover-item">
    <svg viewBox="0 0 94 94" aria-hidden="true"><path d="M22 40h12l30-16v46L34 54H22z" fill="#7ab648"/><path d="M30 54l6 18h8l-4-18" fill="#5e9632"/></svg>
    Promotions</div>
  <div class="cover-item">
    <svg viewBox="0 0 94 94" aria-hidden="true"><rect x="16" y="20" width="62" height="46" fill="none" stroke="#7ab648" stroke-width="5"/><path d="M16 30h62" stroke="#7ab648" stroke-width="5"/><path d="M44 42l18 10-8 2 6 10-4 2-6-10-6 6z" fill="#5e9632"/></svg>
    Pay per Click</div>
  <div class="cover-item">
    <svg viewBox="0 0 94 94" aria-hidden="true"><path d="M30 18h34v60L47 64 30 78z" fill="#7ab648"/></svg>
    Social Bookmarking</div>
</div>
<a class="abs signup-btn">SIGNUP FOR FREE &#10148;</a>

<!-- footer -->
<footer>
  <div class="abs footer-col" style="left:176px;top:2162px">
    <h4>Brovelle</h4>
    <p class="footer-about"><b>Its a Sample text :-</b><br>The idea is that businesses will register with us and will be offered two different kinds of services. They can make use of our scripts to check their back links, rankings, compare with competitors and a number of other marketing tools. The other service we provide is that we offer them an SEO service at a very competitive price. We will handle social networking, link building.</p>
    <p style="text-align:right;width:370px;font-size:10px;color:var(--green);margin-top:6px">LEARN MORE</p>
  </div>
  <div class="abs footer-col" style="left:577px;top:2162px">
    <h4>Resources</h4>
    <ul><li>About us</li><li>Blog</li><li>FAQ</li><li>Services</li><li>Why Choose Brovelle</li></ul>
  </div>
  <div class="abs footer-col" style="left:733px;top:2162px">
    <h4>Services</h4>
    <ul><li>Search Engine Optimization</li><li>Search Engine Marketing</li><li>Blog Optimization</li><li>Research &amp; Analytics</li><li>Social Marketing</li></ul>
  </div>
  <div class="abs footer-col" style="left:907px;top:2162px">
    <h4>Get Social</h4>
    <div class="socials"><span></span><span></span><span></span></div>
  </div>
</footer>
<div class="abs bottom-bar"></div>
<div class="abs bottom-brand"><span class="brand-dot"></span>brovelle.example</div>
<p class="abs copyright">Copyright &copy; 2013-2050 Brovelle Inc. All Rights Reserved.</p>

</body>
</html>
```